I need a logo design and a business card design for a new strategy consultancy that I set up called Tessaron LLC. We help clients make strategically important decisions, cutting through the cloud of noise. The design should imply clarity, simplicity and wisdom.

```html
<!DOCTYPE html>
<html lang="en">
<head>
<meta charset="UTF-8">
<title>Tessaron LLC — Business Cards</title>
<link href="https://fonts.googleapis.com/css2?family=Cinzel:wght@700&family=Lato:wght@400;700&display=swap" rel="stylesheet">
<style>
  :root {
    --brand-blue: #1b98cf;
    --ink-grey: #4a4a4a;
    --rule-grey: #5a5a5a;
    --card-white: #ffffff;
    --backdrop: #e6e8ea;
  }
  * { box-sizing: border-box; margin: 0; padding: 0; }
  html, body { width: 1200px; height: 858px; overflow: hidden; }
  body {
    background: var(--backdrop);
    font-family: "Lato", Arial, sans-serif;
    display: flex;
    align-items: center;
    justify-content: center;
    gap: 40px;
  }
  .card {
    width: 530px;
    height: 303px;
    border-radius: 26px;
    position: relative;
    overflow: hidden;
    box-shadow: 0 10px 28px rgba(0,0,0,0.18);
  }
  /* Front */
  .card--front {
    background: var(--brand-blue);
    color: var(--card-white);
    display: flex;
    flex-direction: column;
    align-items: center;
    justify-content: center;
  }
  .brand {
    display: flex;
    align-items: center;
    gap: 12px;
    font-family: "Cinzel", Georgia, serif;
    font-weight: 700;
    letter-spacing: 1px;
  }
  .brand__dot {
    width: 14px; height: 14px; border-radius: 50%;
    background: currentColor;
  }
  .card--front .brand { font-size: 38px; margin-top: 10px; }
  .front__web {
    font-size: 13px;
    letter-spacing: 2px;
    margin-top: 52px;
  }
  /* Back */
  .card--back {
    background: var(--card-white);
    display: flex;
    align-items: center;
  }
  .back__brand {
    width: 250px;
    display: flex;
    justify-content: center;
  }
  .card--back .brand {
    color: var(--brand-blue);
    font-size: 25px;
  }
  .back__divider {
    width: 1.5px;
    height: 150px;
    background: var(--rule-grey);
  }
  .back__details {
    padding-left: 26px;
    color: var(--ink-grey);
  }
  .person__name {
    font-family: "Cinzel", Georgia, serif;
    font-weight: 700;
    font-size: 22px;
    color: var(--brand-blue);
    line-height: 1;
  }
  .person__role { font-size: 13px; margin-bottom: 14px; }
  .address { font-size: 12.5px; line-height: 1.35; margin-bottom: 12px; }
  .contact-list { list-style: none; font-size: 12.5px; line-height: 1.55; }
  .contact-list li { display: flex; align-items: center; gap: 8px; }
  .contact-list svg { width: 12px; height: 12px; fill: var(--brand-blue); flex: none; }
  .edge-band {
    position: absolute; left: 0; right: 0; bottom: 0; height: 6px;
    display: flex;
  }
  .edge-band__grey { flex: 1; background: var(--rule-grey); }
  .edge-band__blue { width: 46%; background: var(--brand-blue); margin-left: 3px; }
</style>
</head>
<body>
  <section class="card card--front">
    <div class="brand"><span class="brand__dot"></span>TESSARON LLC</div>
    <p class="front__web">www.tessaronllc.com</p>
  </section>

  <section class="card card--back">
    <div class="back__brand">
      <div class="brand"><span class="brand__dot"></span>TESSARON LLC</div>
    </div>
    <div class="back__divider"></div>
    <div class="back__details">
      <h1 class="person__name">DANIEL HART</h1>
      <p class="person__role">Director</p>
      <p class="address">48 Harbour Row, Suite B<br>Leeds, UK LS1 4DP</p>
      <ul class="contact-list">
        <li>
          <svg viewBox="0 0 24 24" aria-hidden="true"><path d="M6.6 10.8a15.1 15.1 0 0 0 6.6 6.6l2.2-2.2c.3-.3.7-.4 1-.2 1.1.4 2.3.6 3.6.6.6 0 1 .4 1 1V20c0 .6-.4 1-1 1C10.6 21 3 13.4 3 4c0-.6.4-1 1-1h3.5c.6 0 1 .4 1 1 0 1.3.2 2.5.6 3.6.1.3 0 .7-.2 1z"/></svg>
          020 555 0147
        </li>
        <li>
          <svg viewBox="0 0 24 24" aria-hidden="true"><path d="M2 5h20v14H2z M2 5l10 8 10-8" /></svg>
          daniel@tessaronllc.com
        </li>
        <li>
          <svg viewBox="0 0 24 24" aria-hidden="true"><path d="M12 2a10 10 0 1 0 0 20 10 10 0 0 0 0-20zm6.9 6h-3a15 15 0 0 0-1.3-4A8 8 0 0 1 18.9 8zM12 4c.8 1.1 1.5 2.5 1.9 4h-3.8c.4-1.5 1.1-2.9 1.9-4zM4.3 14a8 8 0 0 1 0-4h3.4a16 16 0 0 0 0 4zm.8 2h3a15 15 0 0 0 1.3 4A8 8 0 0 1 5.1 16zm3-8h-3a8 8 0 0 1 4.3-4 15 15 0 0 0-1.3 4zM12 20c-.8-1.1-1.5-2.5-1.9-4h3.8c-.4 1.5-1.1 2.9-1.9 4zm2.3-6H9.7a14 14 0 0 1 0-4h4.6a14 14 0 0 1 0 4zm.3 6a15 15 0 0 0 1.3-4h3a8 8 0 0 1-4.3 4zm1.7-6a16 16 0 0 0 0-4h3.4a8 8 0 0 1 0 4z"/></svg>
          www.tessaronllc.com
        </li>
      </ul>
    </div>
    <div class="edge-band"><span class="edge-band__grey"></span><span class="edge-band__blue"></span></div>
  </section>
</body>
</html>
```